Need to drive pregnant women to my 3d4d ultrasound studio where i provide 4d ultrasound with hyperalistic imaging and gender reveals

Industry/Entity Type

Healthcare

Font styles to use
Decorative
Script

Requirements
Must have
• My Company name Luz de Nueve Lunas 4D. EVERYTHING HAS TO BE IN SPANISH
Nice to have
• SIMPLE AND NOT TOO BUSY
Should not have
• website

```html
<!DOCTYPE html>
<html lang="es">
<head>
<meta charset="utf-8">
<title>Luz de Nueve Lunas 4D – Banner</title>
<link rel="stylesheet" href="https://fonts.googleapis.com/css2?family=Great+Vibes&family=Oswald:wght@500;600;700&family=Poppins:wght@400;600;700&display=swap">
<style>
  :root{
    --page:#e3e3e3;
    --violet-top:#b43bbd;
    --violet-mid:#9a3fc6;
    --violet-low:#6f5ad6;
    --plum:#45063f;
    --plum-ink:#3d0a36;
    --pink-soft:#f6b7f0;
    --orchid:#c35fd6;
    --gold:#d9a526;
    --gold-light:#f7dc6f;
    --magenta:#c81fc4;
    --blue:#1d6fc9;
    --white:#ffffff;
    --pin-red:#e3252b;
  }
  *{box-sizing:border-box;margin:0;padding:0}
  html,body{width:1178px;height:1200px;overflow:hidden;background:var(--page)}
  .banner{
    position:absolute;left:39px;top:437px;width:1100px;height:326px;
    background:var(--white);overflow:hidden;
    box-shadow:0 8px 18px rgba(0,0,0,.25);
  }
  .banner__sky{
    position:absolute;left:0;top:0;width:1100px;height:235px;
    background:linear-gradient(180deg,var(--violet-top) 0%,var(--violet-mid) 55%,var(--violet-low) 100%);
  }
  .mother-photo{
    position:absolute;left:828px;top:0;width:272px;height:235px;
    background:linear-gradient(160deg,#e7b1d6 0%,#d99ccb 50%,#b58fd8 100%);
  }
  .brand-seal{
    position:absolute;left:45px;top:26px;width:138px;height:138px;border-radius:50%;
    background:#fbeef8;display:flex;align-items:center;justify-content:center;text-align:center;
    font-family:"Poppins",sans-serif;font-weight:600;font-size:15px;line-height:1.2;color:var(--orchid);
  }
  .tagline{
    position:absolute;left:18px;top:170px;width:190px;text-align:center;
    font-family:"Oswald",sans-serif;font-weight:600;font-size:27px;line-height:.98;color:var(--white);
    text-shadow:0 2px 3px rgba(40,0,60,.45);
  }
  .headline-script{
    position:absolute;left:236px;top:8px;
    font-family:"Great Vibes",cursive;font-size:86px;line-height:1;color:var(--white);
    text-shadow:0 2px 3px rgba(40,0,60,.35);
  }
  .headline-bold{
    position:absolute;left:232px;top:100px;
    font-family:"Oswald",sans-serif;font-weight:700;font-size:62px;line-height:1;color:var(--white);
    text-shadow:0 3px 4px rgba(40,0,60,.35);
  }
  .service-band{
    position:absolute;left:233px;top:175px;width:500px;height:67px;border-radius:12px;
    background:var(--plum);
  }
  .service-band__big{
    position:absolute;left:16px;top:6px;font-family:"Oswald",sans-serif;font-weight:600;
    font-size:48px;line-height:1;color:var(--white);
  }
  .service-band__line1{
    position:absolute;left:78px;top:7px;font-family:"Poppins",sans-serif;font-weight:400;
    font-size:23px;line-height:1.1;color:var(--white);
  }
  .service-band__line2{
    position:absolute;left:78px;top:34px;font-family:"Poppins",sans-serif;font-weight:700;
    font-size:23px;line-height:1.1;color:var(--pink-soft);
  }
  .scan-frame{
    position:absolute;border:5px solid var(--gold);box-shadow:0 3px 6px rgba(0,0,0,.3);
  }
  .scan-frame--one{left:690px;top:30px;width:134px;height:122px;transform:rotate(-3deg);
    background:linear-gradient(135deg,#f0a27c,#c9653f 60%,#6a2a18)}
  .scan-frame--two{left:710px;top:148px;width:134px;height:120px;transform:rotate(-3deg);
    background:linear-gradient(135deg,#f0c2b2,#d8998a 60%,#8a5a52)}
  .gender-badge{position:absolute;left:893px;top:150px;width:152px;height:152px}
  .gender-badge__text{
    position:absolute;left:0;top:0;width:152px;height:152px;display:flex;flex-direction:column;
    align-items:center;justify-content:center;text-align:center;
  }
  .gender-badge__script{font-family:"Great Vibes",cursive;font-size:20px;color:var(--plum-ink);line-height:1}
  .gender-badge__word{font-family:"Oswald",sans-serif;font-weight:700;font-size:32px;line-height:1}
  .gender-badge__word--pink{color:var(--magenta)}
  .gender-badge__word--blue{color:var(--blue)}
  .contact-phone{position:absolute;left:27px;top:259px;display:flex;align-items:center;gap:12px}
  .contact-phone__number{font-family:"Poppins",sans-serif;font-weight:700;font-size:42px;line-height:1;color:var(--plum-ink);letter-spacing:-1px}
  .divider{position:absolute;left:394px;top:254px;height:44px;border-left:2px dashed var(--orchid)}
  .service-area{position:absolute;left:410px;top:256px;display:flex;gap:6px}
  .service-area__lines{font-family:"Poppins",sans-serif;color:var(--plum-ink);line-height:1.05}
  .service-area__lead{font-size:21px;letter-spacing:5px;font-weight:400}
  .service-area__place{font-size:22px;font-weight:700}
  .social{position:absolute;left:716px;top:278px;display:flex;align-items:center;gap:8px;
    font-family:"Poppins",sans-serif;font-weight:600;font-size:12px;letter-spacing:1.5px;color:var(--plum-ink)}
  .social__dot{width:12px;height:12px;border-radius:50%;background:var(--orchid)}
  .social__handle{letter-spacing:.5px;font-weight:600}
</style>
</head>
<body>
  <div class="banner">
    <div class="banner__sky"></div>
    <div class="mother-photo" role="img" aria-label="Foto de mujer embarazada con ropa rosa sosteniendo una ecografía"></div>

    <div class="brand-seal">Luz de<br>Nueve Lunas<br>4D</div>
    <div class="tagline">MOMENTOS<br>INOLVIDABLES</div>

    <div class="headline-script">Luz de</div>
    <div class="headline-bold">NUEVE LUNAS</div>

    <div class="service-band">
      <div class="service-band__big">4D</div>
      <div class="service-band__line1">ULTRASONIDO CON</div>
      <div class="service-band__line2">IMÁGENES HIPERREALISTAS</div>
    </div>

    <div class="scan-frame scan-frame--one" role="img" aria-label="Imagen de ultrasonido 4D de un bebé"></div>
    <div class="scan-frame scan-frame--two" role="img" aria-label="Foto de recién nacido dormido"></div>

    <div class="gender-badge">
      <svg width="152" height="152" viewBox="0 0 152 152" aria-hidden="true">
        <defs>
          <radialGradient id="goldFill" cx="50%" cy="40%" r="60%">
            <stop offset="0" stop-color="#f7dc6f"/>
            <stop offset="1" stop-color="#d9a526"/>
          </radialGradient>
        </defs>
        <polygon fill="url(#goldFill)" stroke="#f3c9ef" stroke-width="2"
          points="76,4 86,14 99,8 105,21 119,20 120,34 133,38 129,51 140,60 132,71 140,82 129,91 133,104 120,108 119,122 105,121 99,134 86,128 76,138 66,128 53,134 47,121 33,122 32,108 19,104 23,91 12,82 20,71 12,60 23,51 19,38 32,34 33,20 47,21 53,8 66,14"/>
      </svg>
      <div class="gender-badge__text">
        <span class="gender-badge__script">Especializado en</span>
        <span class="gender-badge__word gender-badge__word--pink">GÉNERO</span>
        <span class="gender-badge__word gender-badge__word--blue">REVELA</span>
      </div>
    </div>

    <div class="contact-phone">
      <svg width="40" height="40" viewBox="0 0 40 40" aria-hidden="true">
        <circle cx="20" cy="20" r="20" fill="#c35fd6"/>
        <path d="M14 11c1-1 2.5-1 3 .3l1.6 3.6c.4.9 0 1.8-.7 2.3l-1.2.8c1 2.3 2.8 4.1 5.1 5.1l.8-1.2c.5-.7 1.4-1.1 2.3-.7l3.6 1.6c1.3.5 1.3 2 .3 3l-1.6 1.6c-1 1-2.6 1.2-4 .6-4.8-2-8.6-5.8-10.6-10.6-.6-1.4-.4-3 .6-4z" fill="#ffffff"/>
      </svg>
      <span class="contact-phone__number">631-555-0142</span>
    </div>

    <div class="divider"></div>

    <div class="service-area">
      <svg width="14" height="20" viewBox="0 0 14 20" aria-hidden="true" style="margin-top:2px">
        <path d="M7 0a7 7 0 0 0-7 7c0 5 7 13 7 13s7-8 7-13a7 7 0 0 0-7-7zm0 10a3 3 0 1 1 0-6 3 3 0 0 1 0 6z" fill="#e3252b"/>
      </svg>
      <div class="service-area__lines">
        <div class="service-area__lead">SERVIENDO LA</div>
        <div class="service-area__place">AREA OESTE DE PR</div>
      </div>
    </div>

    <div class="social">
      <span>SÍGUENOS EN</span>
      <span class="social__dot"></span>
      <span class="social__handle">@luznuevelunas4d</span>
    </div>
  </div>
</body>
</html>
```